Small Business Consulting Firm Needs Business Card Design

Need a sleek modern business card with 2 sides matching the colors of our logo. We will be placing these with a mailer we are sending out. These business cards will only ever be given to business owners. We operate helping businesses who are struggling with cash flow or finances. If the green and blue design needs to be moved to the right of "Harborline Crest Consulting" for aesthetic purposes that is ok. We will need an editable file if possible. We would like to include the reps name, email, website, and phone number. For now just use Peter Vance, pvance@harborlinecrest.com, www.harborlinecrest.com, and 833-555-0172.

```html
<!DOCTYPE html>
<html lang="en">
<head>
<meta charset="utf-8">
<title>Harborline Crest Consulting – Business Card</title>
<link rel="stylesheet" href="https://fonts.googleapis.com/css2?family=Open+Sans:wght@400;600&display=swap">
<style>
  :root {
    --backdrop: #e6e4e1;
    --card: #2a2c2c;
    --card-back-text: #363838;
    --ink: #ffffff;
    --accent: #6cc04a;
    --rule: #f2f2f2;
  }
  * { box-sizing: border-box; margin: 0; padding: 0; }
  html, body {
    width: 1200px; height: 1000px; overflow: hidden;
    background: var(--backdrop);
    font-family: "Open Sans", Arial, sans-serif;
  }
  .canvas { position: relative; width: 1200px; height: 1000px; }
  .card {
    position: absolute; left: 266px; width: 666px; height: 397px;
    background: var(--card);
    box-shadow: 0 4px 14px rgba(0,0,0,0.25);
  }
  .card--front { top: 74px; }
  .card--back { top: 533px; }

  .brand {
    position: absolute; right: 44px; top: 118px;
    display: flex; align-items: center; gap: 14px;
    color: var(--ink); font-weight: 400; text-transform: uppercase;
  }
  .brand__square { width: 26px; height: 26px; background: var(--accent); }
  .brand__name { font-size: 24px; letter-spacing: 1.5px; line-height: 1.15; text-align: right; }

  .rep { position: absolute; left: 46px; top: 176px; }
  .rep__name { color: var(--accent); font-size: 21px; font-weight: 600; }
  .rep__title { color: var(--ink); font-size: 16.5px; margin-top: 2px; }

  .divider {
    position: absolute; left: 46px; right: 44px; top: 243px;
    height: 2px; background: var(--rule);
  }

  .contacts {
    position: absolute; left: 46px; top: 258px; list-style: none;
    color: var(--ink); font-size: 18px; line-height: 25px;
  }
  .contacts li { display: flex; align-items: center; gap: 6px; }
  .contacts svg { width: 16px; height: 16px; fill: var(--accent); flex: none; }

  .address {
    position: absolute; right: 44px; top: 308px; text-align: right;
    color: var(--ink); font-size: 17px; line-height: 24px; font-style: normal;
  }

  .back-brand {
    position: absolute; inset: 0;
    display: flex; align-items: center; justify-content: center; gap: 16px;
    color: var(--card-back-text); font-size: 28px; font-weight: 400;
    letter-spacing: 2px; text-transform: uppercase;
  }
  .back-brand__square { width: 34px; height: 34px; background: var(--card-back-text); }
</style>
</head>
<body>
<main class="canvas">
  <section class="card card--front" aria-label="Business card front">
    <div class="brand">
      <span class="brand__square"></span>
      <span class="brand__name">Harborline Crest<br>Consulting</span>
    </div>

    <div class="rep">
      <p class="rep__name">Peter Vance</p>
      <p class="rep__title">CEO / Owner</p>
    </div>

    <div class="divider"></div>

    <ul class="contacts">
      <li><svg viewBox="0 0 16 16" aria-hidden="true"><path d="M2 6c0-2 2-3 6-3s6 1 6 3v1h-3V5.5H5V7H2zM4 8h8l2 5H2zM8 9.5a1.5 1.5 0 1 0 0 3 1.5 1.5 0 0 0 0-3z"/></svg>833-555-0172</li>
      <li><svg viewBox="0 0 16 16" aria-hidden="true"><path d="M2 6c0-2 2-3 6-3s6 1 6 3v1h-3V5.5H5V7H2zM4 8h8l2 5H2zM8 9.5a1.5 1.5 0 1 0 0 3 1.5 1.5 0 0 0 0-3z"/></svg>833-555-0172</li>
      <li><svg viewBox="0 0 16 16" aria-hidden="true"><path d="M1 3.5h14v9H1zM2.2 4.5 8 9l5.8-4.5z" fill-rule="evenodd"/></svg>info@harborlinecrest.com</li>
      <li><svg viewBox="0 0 16 16" aria-hidden="true"><path d="M8 1a7 7 0 1 0 0 14A7 7 0 0 0 8 1zm0 1.5c.9 0 1.9 1.9 2.1 4.5H5.9C6.1 4.4 7.1 2.5 8 2.5zM2.6 9h2.3c.1 1.6.5 3 1 3.9A5.5 5.5 0 0 1 2.6 9zm0-2a5.5 5.5 0 0 1 3.3-3.9c-.5.9-.9 2.3-1 3.9zm5.4 6.5c-.9 0-1.9-1.9-2.1-4.5h4.2c-.2 2.6-1.2 4.5-2.1 4.5zm2.1-.6c.5-.9.9-2.3 1-3.9h2.3a5.5 5.5 0 0 1-3.3 3.9zM11.1 7c-.1-1.6-.5-3-1-3.9A5.5 5.5 0 0 1 13.4 7z"/></svg>www.harborlinecrest.com</li>
    </ul>

    <address class="address">214 N. Harbor Street<br>Clearport, Missouri 63190</address>
  </section>

  <section class="card card--back" aria-label="Business card back">
    <div class="back-brand">
      <span class="back-brand__square"></span>
      <span>Harborline Crest Consulting</span>
    </div>
  </section>
</main>
</body>
</html>
```